UK Supplement Company Needs a Label for Diet Protein Powder

We need a new, modern and fresh design for our Diet Protein Powder. Our protein powder is packaged in black plastic tubs (photo attached) and needs an attractive label. We would like to see designs that grab attention and look professional. We're very open to ideas. The label should be 88mm x 365mm. We also prefer PSD format where possible. These alterations could be made once your design is chosen. Have attached photo of our shake ingredients/benefits.
Updates

Need extra days to review

Target Market(s)

Slimmers

Industry/Entity Type

Health And Wellness

Font styles to use
Serif
Sans Serif

Colors

Designer to choose colors to be used in the design.

Requirements
Must have
• Clean, Modern and Professional Look. Eye catching. The flavour, we offer 6 flavours so this must be something we can edit (Flavours are Banana, Chocolate, Chocolate Mint, Strawberry, Toffee and Vanilla).
Nice to have
• Our logo, this can be BRISK Nutrition or just BRISK. Our logo files are attached.
Should not have
• We do not want to see people (faces or bodies) on the design.

```html
<!DOCTYPE html>
<html lang="en">
<head>
<meta charset="utf-8">
<title>BRISK Nutrition – Diet Protein Powder Label</title>
<link rel="stylesheet" href="https://fonts.googleapis.com/css2?family=Cinzel:wght@400;700&family=Montserrat:wght@700;800&family=Libre+Baskerville&display=swap">
<style>
  :root {
    --page: #ffffff;
    --label: #0b0b0b;
    --ink-light: #ffffff;
    --ink-soft: #e6e6e6;
    --accent: #8dc63f;
    --accent-deep: #7ab32e;
    --band-text: #1a1a1a;
    --rule: #6a6a6a;
    --rule-dim: #3c4a2a;
  }
  * { margin: 0; padding: 0; box-sizing: border-box; }
  html, body { width: 894px; height: 1200px; overflow: hidden; background: var(--page); }
  .label {
    position: absolute; left: 17px; top: 317px;
    width: 860px; height: 566px;
    background: var(--label); overflow: hidden;
  }
  .brand-panel { position: absolute; left: 0; top: 0; width: 171px; height: 100%; }
  .brand-name {
    position: absolute; left: 88px; top: 283px;
    transform: translate(-50%, -50%) rotate(-90deg);
    white-space: nowrap;
    font-family: "Montserrat", sans-serif; font-weight: 800;
    font-size: 30px; letter-spacing: 2px; color: var(--ink-light);
  }
  .edge-line { position: absolute; top: 0; height: 100%; width: 3px; background: var(--ink-light); }
  .edge-line--left { left: 171px; }
  .edge-line--right { left: 732px; width: 2px; }
  .edge-line--outer { left: 828px; width: 2px; }
  .edge-line--thin { left: 18px; width: 1px; background: #2b3f5a; }

  .product-title {
    position: absolute; left: 462px; transform: translateX(-50%);
    white-space: nowrap; text-align: center;
    font-family: "Cinzel", serif; line-height: 1;
  }
  .product-title--diet { top: 68px; font-size: 96px; font-weight: 700; color: var(--ink-light); }
  .product-title--protein { top: 176px; font-size: 96px; font-weight: 700; color: var(--ink-light); }
  .product-title--powder { top: 272px; font-size: 92px; font-weight: 400; color: var(--accent); }

  .band-rule { position: absolute; height: 1px; background: var(--rule); }
  .band {
    position: absolute; top: 432px; height: 65px;
    background: linear-gradient(90deg, var(--accent-deep), var(--accent));
    display: flex; flex-direction: column; align-items: center; justify-content: center;
    font-family: "Montserrat", sans-serif; color: var(--band-text); line-height: 1.15;
  }
  .band--calories { left: 175px; width: 263px; clip-path: polygon(0 0, 100% 0, 88% 100%, 0 100%); padding-right: 28px; }
  .band--carbs { left: 466px; width: 266px; clip-path: polygon(12% 0, 100% 0, 100% 100%, 0 100%); padding-left: 28px; }
  .band__value { font-size: 19px; font-weight: 700; }
  .band__unit { font-size: 11px; font-weight: 700; }

  .stats { position: absolute; left: 734px; width: 94px; top: 36px; }
  .stat { text-align: center; font-family: "Cinzel", serif; color: var(--ink-soft); padding: 8px 0; }
  .stat + .stat { border-top: 1px solid var(--rule-dim); }
  .stat__value { font-size: 19px; line-height: 1.15; }
  .stat__name { font-size: 12px; line-height: 1.4; }

  .flavour { position: absolute; left: 736px; top: 428px; width: 92px; text-align: center; }
  .flavour__name { font-family: "Libre Baskerville", serif; font-size: 9px; color: var(--ink-soft); white-space: nowrap; }
  .flavour__art {
    display: block; margin: 8px auto 0; width: 84px; height: 46px; border-radius: 6px;
    background: radial-gradient(circle at 40% 55%, #d8232a, #a5161b 60%, #3f7d21);
  }
</style>
</head>
<body>
  <main class="label">
    <span class="edge-line edge-line--thin"></span>
    <section class="brand-panel">
      <div class="brand-name">BRISK NUTRITION</div>
    </section>
    <span class="edge-line edge-line--left"></span>

    <h1>
      <span class="product-title product-title--diet">Diet</span>
      <span class="product-title product-title--protein">Protein</span>
      <span class="product-title product-title--powder">Powder</span>
    </h1>

    <span class="band-rule" style="left:175px;top:422px;width:263px"></span>
    <span class="band-rule" style="left:490px;top:422px;width:242px"></span>
    <div class="band band--calories"><span class="band__value">117 CALORIES</span><span class="band__unit">PER SERVING</span></div>
    <div class="band band--carbs"><span class="band__value">4.2 CARBS</span><span class="band__unit">PER SERVING</span></div>
    <span class="band-rule" style="left:175px;top:509px;width:240px"></span>
    <span class="band-rule" style="left:466px;top:509px;width:266px"></span>

    <span class="edge-line edge-line--right"></span>
    <ul class="stats">
      <li class="stat"><div class="stat__value">120MG</div><div class="stat__name">Green Tea<br>Extract</div></li>
      <li class="stat"><div class="stat__value">21G</div><div class="stat__name">Protein</div></li>
      <li class="stat"><div class="stat__value">120MG</div><div class="stat__name">Acan<br>Berry</div></li>
      <li class="stat"><div class="stat__value">15MG</div><div class="stat__name">CLA<br>Powder</div></li>
    </ul>
    <div class="flavour">
      <div class="flavour__name">Strawberry Flavour</div>
      <span class="flavour__art" role="img" aria-label="Fresh strawberries with green leaves"></span>
    </div>
    <span class="edge-line edge-line--outer"></span>
  </main>
</body>
</html>
```